I am looking for business cards and letterhead

I want a high-level look for CEO's who want a concierge level leadership consultant and organization development strategist

This needs to go with my brand: simple, elegant, clean. Please improve on this design while using these fonts and colors

Here is my website: CorinneHalvers.com

```html
<!DOCTYPE html>
<html lang="en">
<head>
<meta charset="utf-8">
<title>Corinne Halvers – Business Card</title>
<link rel="stylesheet" href="https://fonts.googleapis.com/css2?family=Montserrat:wght@300;400;700&display=swap">
<style>
  :root {
    --backdrop: #262626;
    --card-black: #161616;
    --card-white: #ffffff;
    --brand-blue: #1f5fb4;
    --brand-gold: #e3c98c;
    --ink-light: #f2f2f2;
  }
  * { margin: 0; padding: 0; box-sizing: border-box; }
  html, body {
    width: 1200px; height: 900px; overflow: hidden;
    background: var(--backdrop);
    font-family: "Montserrat", sans-serif;
  }
  .sheet { position: relative; width: 1200px; height: 900px; }
  .card {
    position: absolute; left: 300px;
    width: 600px; height: 343px;
    border-radius: 34px; overflow: hidden;
    background: var(--card-black);
    box-shadow: 0 10px 30px rgba(0,0,0,0.45);
  }
  .card--front { top: 80px; }
  .card--back { top: 477px; }
  .card__art { position: absolute; inset: 0; }

  .contact {
    position: absolute; left: 40px; top: 38px;
    color: var(--ink-light);
    z-index: 1;
  }
  .contact__name {
    font-weight: 700; font-size: 28px; color: var(--brand-blue);
    letter-spacing: 0.3px; white-space: nowrap;
  }
  .contact__title { font-weight: 300; font-size: 15px; margin-top: 4px; }
  .contact__address { font-weight: 300; font-size: 14px; line-height: 1.45; margin-top: 30px; }
  .contact__list {
    list-style: none; margin-top: 26px;
    font-weight: 300; font-size: 14px; line-height: 1.6;
  }
  .contact__list li { display: flex; align-items: center; gap: 8px; }
  .contact__icon { width: 12px; height: 12px; fill: var(--brand-blue); flex: none; }

  .brand-mark {
    position: absolute; display: flex; align-items: center; justify-content: center;
    border: 3px solid var(--brand-gold); border-radius: 50%;
    font-weight: 400; text-align: center; line-height: 1.2;
    color: var(--brand-blue);
  }
  .brand-mark::before {
    content: ""; position: absolute; inset: 7px;
    border: 2px solid var(--brand-gold); border-radius: 50%;
  }
  .brand-mark--front {
    left: 385px; top: 125px; width: 180px; height: 180px; font-size: 18px;
  }
  .brand-mark--back {
    left: 215px; top: 86px; width: 170px; height: 170px; font-size: 17px;
    background: var(--card-black);
  }
  .back-pattern {
    position: absolute; inset: 0;
    background: radial-gradient(circle at 50% 50%, #2a2a2a 0%, #1d1d1d 45%, #121212 100%);
  }
</style>
</head>
<body>
<main class="sheet">

  <section class="card card--front" aria-label="Business card front">
    <svg class="card__art" viewBox="0 0 600 343" aria-hidden="true">
      <circle cx="465" cy="215" r="178" fill="var(--brand-blue)"/>
      <circle cx="475" cy="215" r="170" fill="var(--card-white)"/>
    </svg>

    <div class="contact">
      <h1 class="contact__name">Corinne Halvers</h1>
      <p class="contact__title">Managing Director</p>
      <p class="contact__address">Your address, City<br>State, Zip 1234</p>
      <ul class="contact__list">
        <li>
          <svg class="contact__icon" viewBox="0 0 12 12"><path d="M2 1h3l1 3-1.5 1a6 6 0 0 0 2.5 2.5L8 6l3 1v3a1 1 0 0 1-1 1A9 9 0 0 1 1 2a1 1 0 0 1 1-1z"/></svg>
          123 456 789
        </li>
        <li>
          <svg class="contact__icon" viewBox="0 0 12 12"><path d="M0 2h12v8H0z M0 2l6 4 6-4" stroke="var(--card-black)" stroke-width="1"/></svg>
          info@CorinneHalvers.com
        </li>
        <li>
          <svg class="contact__icon" viewBox="0 0 12 12"><circle cx="6" cy="6" r="6"/></svg>
          CorinneHalvers.com
        </li>
      </ul>
    </div>

    <div class="brand-mark brand-mark--front">Corinne<br>Halvers</div>
  </section>

  <section class="card card--back" aria-label="Business card back">
    <div class="back-pattern" role="img" aria-label="Fine concentric line pattern radiating from the centre"></div>
    <div class="brand-mark brand-mark--back">Corinne<br>Halvers</div>
  </section>

</main>
</body>
</html>
```